Software company specialized in data analytics and professional services

We need a landing page design for our business. It should include our logo design. It should have multiple sections :
- stylish head
- what we do (data analytics software, professional services)
- contact form

Target Market(s)

Companies, B2B

Industry/Entity Type

Data

Number of Pages Required

1 page

Font styles to use
Sans Serif

Requirements
Must have
• Dark theme
Should not have
• Gradients on buttons

```html
<!DOCTYPE html>
<html lang="en">
<head>
<meta charset="utf-8">
<title>Veltrano — Data Analytics</title>
<link rel="stylesheet" href="https://fonts.googleapis.com/css2?family=Open+Sans:wght@600;700&family=Roboto:wght@400;500&display=swap">
<style>
:root{
  --ink:#ffffff;
  --muted:#e6e3f2;
  --base:#191328;
  --deep:#140f22;
  --footer:#0f0b1b;
  --violet:#7b68d6;
  --violet-dark:#45388a;
  --blue:#3f8fe0;
  --accent:#5a9de0;
  --line:#c9c3e6;
  --btn-dark:#3a3648;
}
*{margin:0;padding:0;box-sizing:border-box}
html,body{width:1200px;height:2188px;overflow:hidden;background:var(--base)}
body{position:relative;font-family:"Roboto",Arial,sans-serif;color:var(--ink)}
.abs{position:absolute}
h1,h2,h3{font-family:"Open Sans",Arial,sans-serif;font-weight:700}
.front{z-index:2}

/* hero */
.hero{left:0;top:0;width:1200px;height:602px;
  background:
    radial-gradient(ellipse 320px 260px at 40px 40px,#3f7aa6 0%,rgba(63,122,166,0) 100%),
    radial-gradient(ellipse 340px 300px at 0px 330px,#6a1e82 0%,rgba(106,30,130,0) 100%),
    radial-gradient(ellipse 420px 300px at 1200px 600px,#2e5a8c 0%,rgba(46,90,140,0) 100%),
    #1c1733}
.logo{font-family:"Roboto",Arial,sans-serif;font-weight:500;letter-spacing:2px;color:var(--ink)}
.nav-logo{left:153px;top:24px;font-size:18px}
.nav{top:30px;font-size:10px;display:flex;align-items:center;gap:3px}
.nav svg{width:9px;height:9px}
.btn{position:absolute;display:flex;align-items:center;justify-content:center;font-size:10px;border-radius:4px;color:var(--ink)}
.btn-login{left:898px;top:24px;width:71px;height:25px;background:var(--btn-dark);border:1px solid #77738a}
.btn-signin{left:976px;top:24px;width:71px;height:24px;background:var(--blue)}
.hero-title{left:154px;top:274px;font-size:29px;line-height:38px;white-space:nowrap}
.hero-sub{left:154px;top:363px;font-size:11.5px;line-height:19px;color:var(--muted)}
.art{border-radius:24px;z-index:1}
.art-hero{left:548px;top:157px;width:502px;height:352px;
  background:radial-gradient(ellipse at 50% 50%,#6b5cc8 0%,#4a3d99 55%,rgba(40,30,90,0) 80%)}

/* what we do */
.wwd{left:0;top:602px;width:1200px;height:432px;background:#1a1229}
.art-wwd{left:155px;top:658px;width:527px;height:331px;
  background:radial-gradient(ellipse at 50% 55%,#6a5bd0 0%,#44389a 55%,rgba(40,30,90,0) 82%)}
.wwd-title{right:153px;top:748px;font-size:30px;text-align:right}
.wwd-text{right:154px;top:795px;width:290px;text-align:right;font-size:11.5px;line-height:19px;color:var(--muted)}
.btn-more{left:969px;top:889px;width:71px;height:25px;background:var(--btn-dark);border:1px solid #77738a}

/* services */
.services{left:0;top:1034px;width:1200px;height:961px;
  background:
    radial-gradient(ellipse 300px 260px at 1200px 80px,#2b4e7a 0%,rgba(43,78,122,0) 100%),
    radial-gradient(ellipse 260px 400px at 0px 560px,#3a2b6a 0%,rgba(58,43,106,0) 100%),
    radial-gradient(ellipse 320px 280px at 0px 960px,#2a5a86 0%,rgba(42,90,134,0) 100%),
    radial-gradient(ellipse 320px 260px at 1200px 960px,#4e1e60 0%,rgba(78,30,96,0) 100%),
    var(--deep)}
.services-title{left:152px;top:1106px;font-size:30px}
.service{width:175px}
.service-head{display:flex;align-items:center;gap:9px;white-space:nowrap}
.service-icon{width:26px;height:26px;border:1px solid #cfcbe0;border-radius:6px;display:flex;align-items:center;justify-content:center;flex:none}
.service-icon svg{width:16px;height:16px}
.service-name{font-family:"Roboto",Arial,sans-serif;font-weight:400;font-size:19px;color:var(--accent)}
.service-text{margin-top:8px;font-size:11.5px;line-height:19px;color:var(--muted)}
.art-services{left:594px;top:1119px;width:459px;height:303px;
  background:radial-gradient(ellipse at 55% 50%,#6e5fd0 0%,#4a3da0 55%,rgba(40,30,90,0) 82%)}

/* contact */
.contact{left:153px;top:1540px;width:894px;height:384px;border:1px solid #8f8aa8;border-radius:3px;overflow:hidden;display:flex}
.form-panel{width:447px;height:100%;position:relative;
  background:radial-gradient(ellipse 260px 200px at 0 384px,#3f5fb0 0%,rgba(63,95,176,0) 100%),var(--violet-dark)}
.info-panel{flex:1;height:100%;position:relative;
  background:linear-gradient(135deg,#1c1628 0%,#241c35 60%,#3a3142 100%)}
.panel-title{position:absolute;left:0;width:100%;top:52px;text-align:center;font-size:22px}
.field{position:absolute;left:45px;width:357px;border-bottom:1px solid var(--line);font-size:11.5px;color:var(--muted);padding-bottom:3px}
.btn-send{left:188px;top:331px;width:71px;height:24px;background:var(--blue)}
.info-row{position:absolute;left:109px;display:flex;align-items:center;gap:14px;font-size:11.5px;color:var(--muted);white-space:nowrap}
.info-row svg{width:18px;height:18px}

/* footer */
.footer{left:0;top:1995px;width:1200px;height:193px;background:var(--footer)}
.copy{left:154px;top:2032px;font-size:11.5px;color:var(--muted)}
.footer-text{left:154px;top:2054px;width:470px;font-size:11.5px;line-height:19px;color:var(--muted)}
.footer-col{top:2032px;font-size:11.5px;line-height:19px;color:var(--muted)}
.footer-col h3{font-family:"Open Sans",Arial,sans-serif;font-size:11px;font-weight:700;color:var(--ink);margin-bottom:4px}
.footer-rule{left:153px;top:2125px;width:894px;height:1px;background:#8f8aa8}
.footer-logo{left:152px;top:2142px;font-size:13px}
</style>
</head>
<body>

<section class="abs hero">
  <div class="abs logo nav-logo">VELTRANO</div>
  <nav>
    <span class="abs nav" style="left:419px">Home <svg viewBox="0 0 10 10"><path d="M1 3l4 4 4-4" fill="none" stroke="#fff" stroke-width="1.4"/></svg></span>
    <span class="abs nav" style="left:507px">What We Do <svg viewBox="0 0 10 10"><path d="M1 3l4 4 4-4" fill="none" stroke="#fff" stroke-width="1.4"/></svg></span>
    <span class="abs nav" style="left:622px">Services <svg viewBox="0 0 10 10"><path d="M1 3l4 4 4-4" fill="none" stroke="#fff" stroke-width="1.4"/></svg></span>
    <span class="abs nav" style="left:720px">Contact Us <svg viewBox="0 0 10 10"><path d="M1 3l4 4 4-4" fill="none" stroke="#fff" stroke-width="1.4"/></svg></span>
  </nav>
  <a class="btn btn-login">Log in</a>
  <a class="btn btn-signin">Sign in</a>
</section>
<div class="abs art art-hero" role="img" aria-label="3D illustration of rising bar chart with magnifying glass, arrow and pie chart"></div>
<h1 class="abs front hero-title">Where powerful analytics<br>meets simplicity.</h1>
<p class="abs front hero-sub">Discover a new era of data-driven<br>decisions with Veltrano</p>

<section class="abs wwd"></section>
<div class="abs art art-wwd" role="img" aria-label="3D illustration of briefcase, target with dart and bar chart"></div>
<h2 class="abs front wwd-title">What We Do</h2>
<p class="abs front wwd-text">Veltrano provides comprehensive analytical services for software data, delivering sophisticated insights and assessments to facilitate informed decision-making within the realm of software operations.</p>
<a class="btn front btn-more">See more</a>

<section class="abs services"></section>
<h2 class="abs front services-title">Our Services</h2>
<div class="abs front service" style="left:153px;top:1165px">
  <div class="service-head"><span class="service-icon"><svg viewBox="0 0 16 16"><circle cx="7" cy="7" r="5" fill="none" stroke="#fff" stroke-width="1.2"/><path d="M11 11l4 4M4 8l2-2 2 2 2-3" fill="none" stroke="#fff" stroke-width="1.2"/></svg></span><h3 class="service-name">Lorem ipsum</h3></div>
  <p class="service-text">Lorem ipsum dolor sit amet, consectetur adipiscing elit, sed do eiusmod tempor incididunt ut labore et dolore magna aliqua.</p>
</div>
<div class="abs front service" style="left:373px;top:1165px">
  <div class="service-head"><span class="service-icon"><svg viewBox="0 0 16 16"><circle cx="7" cy="9" r="5" fill="none" stroke="#fff" stroke-width="1.2"/><path d="M7 9V4M7 9h5M9 2a5 5 0 0 1 5 5H9z" fill="none" stroke="#fff" stroke-width="1.2"/></svg></span><h3 class="service-name">Lorem ipsum</h3></div>
  <p class="service-text">Lorem ipsum dolor sit amet, consectetur adipiscing elit, sed do eiusmod tempor incididunt ut labore et dolore magna aliqua.</p>
</div>
<div class="abs front service" style="left:153px;top:1311px">
  <div class="service-head"><span class="service-icon"><svg viewBox="0 0 16 16"><path d="M3 2h8v8M3 2v12h6M5 5h4M5 7.5h4" fill="none" stroke="#fff" stroke-width="1.2"/><circle cx="11" cy="11" r="2.5" fill="none" stroke="#fff" stroke-width="1.2"/><path d="M13 13l2 2" stroke="#fff" stroke-width="1.2"/></svg></span><h3 class="service-name">Lorem ipsum</h3></div>
  <p class="service-text">Lorem ipsum dolor sit amet, consectetur adipiscing elit, sed do eiusmod tempor incididunt ut labore et dolore magna aliqua.</p>
</div>
<div class="abs front service" style="left:373px;top:1311px">
  <div class="service-head"><span class="service-icon"><svg viewBox="0 0 16 16"><rect x="2" y="2" width="12" height="12" rx="3" fill="none" stroke="#fff" stroke-width="1.2"/><path d="M5.5 11V8M8 11V5M10.5 11V7" stroke="#fff" stroke-width="1.2"/></svg></span><h3 class="service-name">Lorem ipsum</h3></div>
  <p class="service-text">Lorem ipsum dolor sit amet, consectetur adipiscing elit, sed do eiusmod tempor incididunt ut labore et dolore magna aliqua.</p>
</div>
<div class="abs art art-services" role="img" aria-label="3D illustration of report board with bar chart, magnifying glass and pie chart"></div>

<section class="abs contact">
  <form class="form-panel">
    <h2 class="panel-title">Send Us A Message</h2>
    <div class="field" style="top:95px">Name</div>
    <div class="field" style="top:131px">Email</div>
    <div class="field" style="top:166px">Subject</div>
    <div class="field" style="top:201px;height:106px">Message</div>
    <a class="btn btn-send">Send</a>
  </form>
  <div class="info-panel">
    <h2 class="panel-title">Contact Us</h2>
    <div class="info-row" style="top:125px"><svg viewBox="0 0 18 18"><path d="M9 16s-5-5-5-9a5 5 0 0 1 10 0c0 4-5 9-5 9z" fill="none" stroke="#fff" stroke-width="1.2"/><circle cx="9" cy="7" r="2" fill="none" stroke="#fff" stroke-width="1.2"/></svg>418 Maple Ridge Road Lakewood Ohio 44107</div>
    <div class="info-row" style="top:162px"><svg viewBox="0 0 18 18"><path d="M4 2l3 3-2 2c1 2 3 4 5 5l2-2 3 3-2 2C8 15 3 10 2 4z" fill="none" stroke="#fff" stroke-width="1.2" stroke-linejoin="round"/></svg>+1&nbsp; 555-014-2273</div>
    <div class="info-row" style="top:197px"><svg viewBox="0 0 18 18"><rect x="2" y="4" width="14" height="10" fill="none" stroke="#fff" stroke-width="1.2"/><path d="M2 4l7 6 7-6" fill="none" stroke="#fff" stroke-width="1.2"/></svg>hello@veltrano.example</div>
  </div>
</section>

<footer class="abs footer"></footer>
<p class="abs copy">© 2003 Veltrano&nbsp; All rights reserved</p>
<p class="abs footer-text">Duis aute irure dolor in reprehenderit in voluptate velit esse cillum dolore eu fugiat nulla pariatur. Excepteur sint occaecat cupidatat non proident, sunt in culpa qui officia deserunt mollit anim id est laborum.</p>
<div class="abs footer-col" style="left:837px"><h3>Deus Dopamet</h3>What We Do<br>Our Service<br>Contact Us</div>
<div class="abs footer-col" style="left:954px"><h3>Deus Dopamet</h3>Term of Services<br>Term of Services<br>Term of Services</div>
<div class="abs footer-rule"></div>
<div class="abs logo footer-logo">VELTRANO</div>

</body>
</html>
```